Business Card - Professional Minimalist - Double sided

We appreciate minimalist logo/web/collateral designs that allow design to tell a story. We want to relay a professional image/approach but throwing in a splash of modern when we’re able so long as it’s not distracting. Think 75% classic corporate, 25% modern. Open to black or white design, not sure which might look the best.

Target Market(s)

Senior executives or related government affairs contacts within the agriculture, energy, and defense industries (i.e., potential clients) but located outside of Washington, DC. Most potential clients based in DC with be familiar with both of us and our shared history.

Industry/Entity Type

Consulting

Contact Information for Business Card

Name: Daniel R. Whitlock
Title: Co-Founder & Partner
Address: 418 Bramblewood Ave. SE | Suite 2716 | Washington, D.C. 20019
Phone: (202) 555-0187
Email: Daniel@HollerbyWhitlock.com

Font styles to use
Serif

Colors

Designer to choose only greyscale colors for use in the design.

Requirements
Must have
• Name: Daniel R. Whitlock
Phone: (202) 555-0187

```html
<!DOCTYPE html>
<html lang="en">
<head>
<meta charset="utf-8">
<title>Hollerby Whitlock Group – Business Card</title>
<link href="https://fonts.googleapis.com/css2?family=Marcellus&family=Crimson+Text:wght@400;700&display=swap" rel="stylesheet">
<style>
  :root {
    --backdrop: #a3a4a6;
    --card: #000000;
    --mark-grey: #58585b;
    --rule: #a7a8aa;
    --text-light: #ffffff;
    --name-grey: #5e5e61;
  }
  * { margin: 0; padding: 0; box-sizing: border-box; }
  html, body {
    width: 1200px; height: 1200px; overflow: hidden;
    background: var(--backdrop);
  }
  .canvas { position: relative; width: 1200px; height: 1200px; }
  .card {
    position: absolute; left: 226px; width: 809px; height: 463px;
    background: var(--card); overflow: hidden;
  }
  .card--front { top: 111px; }
  .card--back { top: 638px; }

  .brand-square {
    position: absolute; left: 63px; top: 54px;
    width: 96px; height: 96px; background: var(--mark-grey);
  }
  .wordmark {
    position: absolute; right: 63px;
    font-family: "Marcellus", serif; font-weight: 400;
    color: var(--mark-grey); text-align: right; line-height: 1;
  }
  .wordmark__name { display: block; font-size: 45px; letter-spacing: 1px; }
  .wordmark__group { display: block; font-size: 26px; letter-spacing: 15px; margin-right: -15px; margin-top: 14px; }
  .card--front .wordmark { top: 60px; }
  .card--back .wordmark { top: 360px; right: 43px; }

  .person { position: absolute; left: 63px; top: 293px; font-family: "Crimson Text", serif; }
  .person__name { font-size: 28px; font-weight: 700; color: var(--name-grey); letter-spacing: 0.5px; line-height: 1; }
  .person__title { font-size: 19px; color: var(--text-light); margin-top: 6px; line-height: 1; }

  .divider { position: absolute; left: 63px; right: 63px; top: 355px; height: 1px; background: var(--rule); }

  .contact {
    position: absolute; top: 368px; font-family: "Crimson Text", serif;
    font-size: 19px; line-height: 25px; color: var(--text-light);
  }
  .contact--direct { left: 63px; }
  .contact--address { right: 63px; text-align: right; }

  .back-square {
    position: absolute; left: 0; bottom: 0;
    width: 230px; height: 230px; background: var(--mark-grey);
  }
</style>
</head>
<body>
<main class="canvas">
  <section class="card card--front">
    <div class="brand-square"></div>
    <div class="wordmark">
      <span class="wordmark__name">HOLLERBY WHITLOCK</span>
      <span class="wordmark__group">GROUP</span>
    </div>
    <div class="person">
      <p class="person__name">DANIEL R. WHITLOCK</p>
      <p class="person__title">Co-Founder &amp; Partner</p>
    </div>
    <div class="divider"></div>
    <div class="contact contact--direct">
      <p>(202) 555-0187</p>
      <p>Daniel@HollerbyWhitlock.com</p>
    </div>
    <div class="contact contact--address">
      <p>418 Bramblewood Ave. SE | Suite 2716</p>
      <p>Washington, D.C. 20019</p>
    </div>
  </section>

  <section class="card card--back">
    <div class="back-square"></div>
    <div class="wordmark">
      <span class="wordmark__name">HOLLERBY WHITLOCK</span>
      <span class="wordmark__group">GROUP</span>
    </div>
  </section>
</main>
</body>
</html>
```